Lena Corvell Business Card

I need a business card that reflects my current website: itslenacorvell.example and screenshot attached. If we keep the color scheme of the site and sample card below that would be ideal. The business card should include the information on the attached sample cards.

Industry/Entity Type

Business

```html
<!DOCTYPE html>
<html lang="en">
<head>
<meta charset="UTF-8">
<title>Lena Corvell Business Card</title>
<link rel="stylesheet" href="https://fonts.googleapis.com/css2?family=Quicksand:wght@300;400;500&display=swap">
<style>
  :root {
    --backdrop: #1b1b1c;
    --teal: #5cbfb1;
    --teal-mid: #8fd3c9;
    --teal-light: #c3e8e2;
    --teal-pale: #e4f4f1;
    --paper: #ffffff;
    --ink-light: #ffffff;
  }
  * { box-sizing: border-box; margin: 0; padding: 0; }
  html, body {
    width: 1200px;
    height: 800px;
    overflow: hidden;
    background: var(--backdrop);
    font-family: "Quicksand", sans-serif;
  }
  .canvas {
    width: 1200px;
    height: 800px;
    display: flex;
    flex-direction: column;
    align-items: center;
    justify-content: center;
    gap: 40px;
  }
  .card {
    position: relative;
    width: 560px;
    height: 320px;
    overflow: hidden;
    background: var(--paper);
  }
  .card-front .decor-area {
    position: absolute;
    inset: 0;
    background: linear-gradient(115deg, var(--paper) 0%, var(--teal-pale) 22%, var(--teal-light) 42%, var(--teal-mid) 60%, var(--teal) 80%, var(--teal) 100%);
  }
  .card-front .wordmark {
    position: absolute;
    right: 54px;
    top: 136px;
    color: var(--ink-light);
    font-size: 32px;
    font-weight: 500;
    letter-spacing: 0.5px;
    white-space: nowrap;
  }
  .card-back {
    background: linear-gradient(28deg, var(--teal) 0%, var(--teal) 38%, var(--teal-mid) 62%, var(--teal-pale) 84%, var(--paper) 100%);
    color: var(--ink-light);
    padding: 70px 0 0 62px;
  }
  .card-back .name {
    font-size: 40px;
    font-weight: 300;
    letter-spacing: 2px;
    line-height: 1;
  }
  .card-back .roles {
    margin-top: 8px;
    font-size: 9.5px;
    font-weight: 400;
    letter-spacing: 0.6px;
  }
  .contact-list {
    list-style: none;
    margin-top: 52px;
    display: flex;
    flex-direction: column;
    gap: 12px;
  }
  .contact-item {
    display: flex;
    align-items: center;
    gap: 12px;
    font-size: 15.5px;
    font-weight: 400;
    letter-spacing: 0.8px;
  }
  .contact-icon {
    width: 18px;
    height: 14px;
    flex: none;
  }
  .handle-mark {
    width: 12px;
    height: 12px;
    margin: 0 3px;
    border: 1.5px solid var(--ink-light);
    border-radius: 3px;
    flex: none;
  }
</style>
</head>
<body>
<main class="canvas">
  <section class="card card-front" aria-label="Card front">
    <div class="decor-area" role="img" aria-label="Decorative layered teal background"></div>
    <div class="wordmark">Lena Corvell</div>
  </section>

  <section class="card card-back" aria-label="Card back">
    <h1 class="name">Lena Corvell</h1>
    <p class="roles">Brand Curator | Digital Storyteller | Social Entrepreneur</p>
    <ul class="contact-list">
      <li class="contact-item">
        <svg class="contact-icon" viewBox="0 0 18 14" aria-hidden="true">
          <circle cx="9" cy="7" r="6" fill="none" stroke="#fff" stroke-width="1.4"/>
          <path d="M3 7 H15 M9 1 C6 4 6 10 9 13 M9 1 C12 4 12 10 9 13" fill="none" stroke="#fff" stroke-width="1.1"/>
        </svg>
        <span>www.itslenacorvell.example</span>
      </li>
      <li class="contact-item">
        <svg class="contact-icon" viewBox="0 0 18 14" aria-hidden="true">
          <rect x="1" y="1.5" width="16" height="11" fill="none" stroke="#fff" stroke-width="1.4"/>
          <path d="M1 1.5 L9 8 L17 1.5" fill="none" stroke="#fff" stroke-width="1.4"/>
        </svg>
        <span>me@lenacorvell.example</span>
      </li>
      <li class="contact-item">
        <span class="handle-mark" aria-hidden="true"></span>
        <span>@itslenacorvell</span>
      </li>
    </ul>
  </section>
</main>
</body>
</html>
```